QRV In Home Flier

To prepare a flier to be placed directly into existing clients homes, which shares additional services available. These are clients that are using QRV Cleaning services and we want to use our QRV Pest Control or BWO (Bondo Mend Up)Maintenance Services

Target Market(s)

residential home owners / Renters

Industry/Entity Type

Property Maintenance

Colors

Designer to choose colors to be used in the design.

Requirements
Must have
• Must be crisp and clean - design should pop - A CLEAR call to action
Nice to have
• See previous designed uploaded
Should not have

```html
<!DOCTYPE html>
<html lang="en">
<head>
<meta charset="utf-8">
<title>QRV Home Maintenance Flier</title>
<link rel="stylesheet" href="https://fonts.googleapis.com/css2?family=Oswald:wght@600&family=Open+Sans:wght@400;600;700&display=swap">
<style>
  :root {
    --brand-blue: #2f7fc4;
    --brand-blue-dark: #1f68a8;
    --accent-orange: #f7941d;
    --ink: #1c2430;
    --text-gray: #6d6e71;
    --paper: #ffffff;
    --cream: #ece7d9;
  }
  html, body {
    margin: 0;
    padding: 0;
    width: 800px;
    height: 1200px;
    overflow: hidden;
    background: var(--paper);
  }
  .flier {
    position: relative;
    width: 800px;
    height: 1200px;
    overflow: hidden;
    background: var(--paper);
    font-family: "Open Sans", Arial, sans-serif;
    color: var(--text-gray);
  }
  .backdrop {
    position: absolute;
    inset: 0;
  }
  .brand {
    position: absolute;
    left: 56px;
    top: 52px;
    display: flex;
    align-items: center;
    gap: 14px;
  }
  .brand-dot {
    width: 46px;
    height: 46px;
    border-radius: 50%;
    background: var(--brand-blue);
  }
  .brand-name {
    font-family: "Open Sans", Arial, sans-serif;
    font-weight: 600;
    font-size: 46px;
    letter-spacing: 3px;
    color: var(--ink);
  }
  .hero-title {
    position: absolute;
    left: 48px;
    top: 238px;
    width: 340px;
  }
  .hero-title .headline {
    font-family: "Oswald", Impact, sans-serif;
    font-weight: 600;
    font-size: 92px;
    line-height: 1;
    color: var(--paper);
    margin: 0;
  }
  .hero-title .subhead {
    font-size: 50px;
    line-height: 1.05;
    color: var(--ink);
    margin: 4px 0 8px;
    font-weight: 400;
    letter-spacing: -0.5px;
  }
  .hero-title .tagline {
    font-size: 21px;
    line-height: 1.25;
    color: var(--paper);
    margin: 0;
  }
  .hero-title .promise {
    font-size: 21px;
    font-weight: 700;
    color: var(--ink);
    margin: 2px 0 0;
  }
  .emergency {
    position: absolute;
    left: 48px;
    top: 634px;
    font-size: 22px;
    font-weight: 600;
    line-height: 1.35;
    color: var(--text-gray);
    margin: 0;
  }
  .services {
    position: absolute;
    left: 46px;
    top: 770px;
    display: grid;
    grid-template-columns: 248px 240px;
    row-gap: 28px;
    margin: 0;
    padding: 0;
    list-style: none;
  }
  .service {
    display: flex;
    align-items: center;
    gap: 10px;
    font-size: 22px;
    font-weight: 600;
    line-height: 1.2;
    color: var(--text-gray);
  }
  .service svg { flex: none; }
  .incentive {
    position: absolute;
    left: 558px;
    top: 818px;
    width: 196px;
    height: 196px;
    border-radius: 50%;
    background: var(--accent-orange);
    border: 4px solid var(--paper);
    box-sizing: border-box;
    display: flex;
    align-items: center;
    justify-content: center;
    text-align: center;
    font-weight: 700;
    font-size: 25px;
    line-height: 1.22;
    color: var(--ink);
  }
  .about {
    position: absolute;
    left: 48px;
    width: 500px;
    font-size: 14px;
    line-height: 1.45;
    text-align: justify;
    color: var(--text-gray);
    margin: 0;
  }
  .about-lead { top: 962px; }
  .about-close { top: 1036px; width: 470px; text-align: left; }
  .web {
    position: absolute;
    left: 48px;
    top: 1140px;
    font-size: 22px;
    font-weight: 700;
    color: var(--paper);
    margin: 0;
  }
  .call {
    position: absolute;
    left: 564px;
    top: 1036px;
    width: 200px;
    text-align: center;
    color: var(--paper);
    font-weight: 700;
    font-size: 17px;
    line-height: 1.28;
    margin: 0;
  }
  .call .vanity {
    display: block;
    font-size: 28px;
    line-height: 1.2;
  }
</style>
</head>
<body>
<main class="flier">
  <svg class="backdrop" width="800" height="1200" viewBox="0 0 800 1200">
    <defs>
      <linearGradient id="photoTone" x1="0" y1="0" x2="1" y2="0">
        <stop offset="0" stop-color="#f3f0e6"/>
        <stop offset="0.45" stop-color="#e4dcc6"/>
        <stop offset="0.7" stop-color="#b89a6c"/>
        <stop offset="1" stop-color="#7f95ad"/>
      </linearGradient>
      <linearGradient id="plumbTone" x1="0" y1="0" x2="1" y2="1">
        <stop offset="0" stop-color="#c9c9c9"/>
        <stop offset="1" stop-color="#6d6a66"/>
      </linearGradient>
      <linearGradient id="electricTone" x1="0" y1="0" x2="1" y2="1">
        <stop offset="0" stop-color="#d9dde2"/>
        <stop offset="1" stop-color="#8b9098"/>
      </linearGradient>
      <linearGradient id="acTone" x1="0" y1="0" x2="1" y2="1">
        <stop offset="0" stop-color="#f1eee8"/>
        <stop offset="1" stop-color="#b9c6b8"/>
      </linearGradient>
    </defs>

    <path class="hero-photo" role="img" aria-label="Photo of a handyman wearing a tool belt full of screwdrivers and pliers"
          d="M0 0 H800 V560 C620 600 420 590 0 610 Z" fill="url(#photoTone)"/>

    <circle class="hero-disc" cx="200" cy="384" r="202" fill="var(--brand-blue)"/>

    <circle class="service-photo" role="img" aria-label="Photo of a plumber fitting a chrome pipe" cx="439" cy="612" r="86" fill="url(#plumbTone)" stroke="#ffffff" stroke-width="5"/>
    <circle class="service-photo" role="img" aria-label="Photo of an electrician testing a fuse board" cx="640" cy="548" r="76" fill="url(#electricTone)" stroke="#ffffff" stroke-width="5"/>
    <circle class="service-photo" role="img" aria-label="Photo of an air conditioning unit being serviced" cx="592" cy="727" r="82" fill="url(#acTone)" stroke="#ffffff" stroke-width="5"/>

    <path class="footer-band" d="M0 1108 H470 C520 1108 540 1062 585 1036 C640 1004 720 996 800 992 V1200 H0 Z" fill="var(--brand-blue)"/>
  </svg>

  <div class="brand">
    <span class="brand-dot"></span>
    <span class="brand-name">QRV</span>
  </div>

  <div class="hero-title">
    <h1 class="headline">Home</h1>
    <p class="subhead">Maintenance</p>
    <p class="tagline">European managed<br>Annual maintenance contracts<br>On call service</p>
    <p class="promise">Your property, our priority.</p>
  </div>

  <p class="emergency">24 Hours<br>Emergency Services</p>

  <ul class="services">
    <li class="service">
      <svg width="42" height="42" viewBox="0 0 42 42" aria-hidden="true">
        <circle cx="21" cy="21" r="19" fill="none" stroke="#1c2430" stroke-width="2"/>
        <rect x="9" y="13" width="24" height="11" rx="2" fill="#1c2430"/>
        <path d="M14 28 l-2 4 M21 28 v4 M28 28 l2 4" stroke="#1c2430" stroke-width="2" stroke-linecap="round"/>
      </svg>
      <span>Ac<br>Services</span>
    </li>
    <li class="service">
      <svg width="42" height="42" viewBox="0 0 42 42" aria-hidden="true">
        <circle cx="21" cy="21" r="19" fill="none" stroke="#1c2430" stroke-width="2"/>
        <path d="M10 14 h12 v-3 h4 v3 h4 v6 h-8 v5 h-6 v-5 h-6 Z" fill="#1c2430"/>
        <circle cx="19" cy="31" r="2" fill="#1c2430"/>
      </svg>
      <span>Electrical<br>Services</span>
    </li>
    <li class="service">
      <svg width="42" height="42" viewBox="0 0 42 42" aria-hidden="true">
        <circle cx="21" cy="21" r="19" fill="none" stroke="#1c2430" stroke-width="2"/>
        <path d="M9 15 h14 a6 6 0 0 1 6 6 v3 h-5 v-3 h-15 Z" fill="#1c2430"/>
        <rect x="15" y="10" width="4" height="5" fill="#1c2430"/>
        <path d="M26.5 28 q-2 3 0 4 q2 -1 0 -4 Z" fill="#1c2430"/>
      </svg>
      <span>Plumbing<br>Services</span>
    </li>
    <li class="service">
      <svg width="42" height="42" viewBox="0 0 42 42" aria-hidden="true">
        <circle cx="21" cy="21" r="19" fill="none" stroke="#1c2430" stroke-width="2"/>
        <circle cx="17" cy="23" r="7" fill="none" stroke="#1c2430" stroke-width="4" stroke-dasharray="3 2.5"/>
        <circle cx="17" cy="23" r="2.5" fill="#1c2430"/>
        <path d="M24 16 l7 -7" stroke="#1c2430" stroke-width="3.5" stroke-linecap="round"/>
      </svg>
      <span>Handyman<br>Services</span>
    </li>
  </ul>

  <div class="incentive">SPECIAL<br>INCENTIVE<br>FOR QRV<br>CLIENT</div>

  <p class="about about-lead">QRV Maintenance Services is reinventing the pest control service industry in Dubai, with GPS technology and world class inventory managment.</p>
  <p class="about about-close">This means you get the right technician, with the right tools at the right time!</p>

  <p class="web">www.qrvhomehelp.com</p>

  <p class="call">Call us now for a<br>FREE ESTIMATE!<span class="vanity">800 Handy</span>+971 04 555 0142<br>+971 56 555 0198</p>
</main>
</body>
</html>
```